Design a New Business Card for Our Company

We are looking for fresh, unique, and a modern business card that reflects our roots as digital marketing agency focused on SEM.

Industry/Entity Type

Marketing

Contact Information for Business Card

looking for very unique out of the box designs. clean and modern that compliments our logo

Requirements
Must have
• colors should match our logo
• Front should have name, address, email, and phone/fax of the person, phone/fax are the same number
• back should have our url

```html
<!DOCTYPE html>
<html lang="en">
<head>
<meta charset="utf-8">
<title>Brightpath Solutions – Business Card</title>
<link href="https://fonts.googleapis.com/css2?family=Lato:wght@400;700&display=swap" rel="stylesheet">
<style>
  :root {
    --backdrop: #ececec;
    --card: #ffffff;
    --brand-blue: #5b93d6;
    --ink: #3b3b3b;
    --ink-soft: #555555;
    --divider: #c9c9c9;
  }
  * { box-sizing: border-box; margin: 0; padding: 0; }
  html, body {
    width: 1200px; height: 1195px; overflow: hidden;
    background: var(--backdrop);
    font-family: "Lato", sans-serif;
  }
  .card {
    position: absolute;
    left: 290px;
    width: 620px; height: 372px;
    background: var(--card);
    overflow: hidden;
  }
  .card--front { top: 162px; }
  .card--back { top: 671px; }

  .brand {
    position: absolute; left: 0; right: 0;
    display: flex; align-items: center; justify-content: center;
    color: var(--brand-blue);
    font-weight: 700;
    white-space: nowrap;
    line-height: 1;
  }
  .brand__dot { border-radius: 50%; background: var(--brand-blue); flex: none; }
  .card--front .brand { top: 74px; font-size: 30px; gap: 10px; }
  .card--front .brand__dot { width: 28px; height: 28px; }
  .card--back .brand { top: 146px; font-size: 46px; gap: 16px; }
  .card--back .brand__dot { width: 44px; height: 44px; }

  .person {
    position: absolute; top: 202px; right: 388px;
    text-align: right; white-space: nowrap;
  }
  .person__name { color: var(--brand-blue); font-weight: 700; font-size: 22px; line-height: 28px; }
  .person__title { color: #111; font-size: 15px; line-height: 20px; }
  .person__address {
    margin-top: 34px;
    color: var(--brand-blue); font-weight: 700; font-size: 15px; line-height: 21px;
  }

  .divider {
    position: absolute; left: 268px; top: 212px;
    width: 3px; height: 110px;
    background: linear-gradient(to bottom, transparent, var(--divider) 30%, var(--divider) 70%, transparent);
  }

  .contacts {
    position: absolute; left: 310px; top: 207px;
    list-style: none;
  }
  .contacts li {
    display: flex; align-items: center; gap: 9px;
    height: 30px;
    color: var(--ink); font-weight: 700; font-size: 15.5px;
    white-space: nowrap;
  }
  .contacts svg { width: 16px; height: 16px; flex: none; fill: var(--brand-blue); }
  .contacts .icon-link { fill: none; stroke: var(--brand-blue); stroke-width: 1.6; }

  .slogan {
    position: absolute; left: 0; right: 0; top: 320px;
    text-align: center;
    color: var(--ink-soft); font-size: 15px; letter-spacing: 3px;
  }
</style>
</head>
<body>

<section class="card card--front" aria-label="Business card front">
  <div class="brand"><span class="brand__dot"></span>Brightpath Solutions</div>

  <div class="person">
    <p class="person__name">Daniel Marsh</p>
    <p class="person__title">Chief Operating Officer</p>
    <p class="person__address">482 Alder Lane,<br>Fairview, PA 16415</p>
  </div>

  <div class="divider"></div>

  <ul class="contacts">
    <li>
      <svg viewBox="0 0 16 16" aria-hidden="true"><path d="M1 6c0-2 3-3.5 7-3.5S15 4 15 6l-3 1-1-2H5L4 7 1 6zm3 2h8l2 5H2l2-5zm4 1.2a1.8 1.8 0 100 3.6 1.8 1.8 0 000-3.6z"/></svg>
      555-214-3380
    </li>
    <li>
      <svg viewBox="0 0 16 16" aria-hidden="true"><path d="M4 1h8v4H4zM1 6h14v6h-3v3H4v-3H1zm4 5v3h6v-3z"/></svg>
      555-214-3382
    </li>
    <li>
      <svg viewBox="0 0 16 16" aria-hidden="true"><path d="M1 3h14v10H1zm1.5 1.5v.3L8 9l5.5-4.2v-.3zm0 2.2v4.8h11V6.7L8 11z"/></svg>
      hello@brightpathsolutions.com
    </li>
    <li>
      <svg class="icon-link" viewBox="0 0 16 16" aria-hidden="true"><path d="M7 9l3-3M6 7L4 9a2 2 0 003 3l2-2M10 9l2-2a2 2 0 00-3-3L7 6"/></svg>
      www.brightpathsolutions.com
    </li>
  </ul>
</section>

<section class="card card--back" aria-label="Business card back">
  <div class="brand"><span class="brand__dot"></span>Brightpath Solutions</div>
  <p class="slogan">Your Slogan / Tagline here</p>
</section>

</body>
</html>
```